Web site for Velto Grounded Consulting Pty. Ltd.

Create a modern website that is contemporary and appropriate for a business that is a provider of Consulting services to businesses. The LOGO is provided below. The consulting services offered are Supply Chain Management, 4th Party Logistics, Sales Coaching and training, HR services and training (i.e. Sexual Harassment and Bullying policies etc. ) , OH&S Training, Management mentoring, Business strategy and tactical consultations and Union related contract negotiations with award inclusion.

Target Market(s)

Importers, Exporters, Manufacturers, Freight Forwarders, Companies with large sales teams, warehouse operators

Industry/Entity Type

Business

Coding

Coded - Design and coding required

Number of Pages Required

5+ page

Font styles to use
Serif
Sans Serif

Colors

Designer to choose colors to be used in the design.

Requirements
Must have
• Sky Line Photographs of Sydney and Manhattan, Pictures of people and teams in professional settings with tasteful clothing. Elements of both femininity and masculinity. People photos need to be diverse and include multiple nationalities, races and genders. Must have blog spot and also include the background info of the owners. Linked In pages includes.
Nice to have
• Would like to try both color and / or black and white.
Should not have
• Open

```html
<!DOCTYPE html>
<html lang="en">
<head>
<meta charset="utf-8">
<title>Velto Grounded Consulting</title>
<link href="https://fonts.googleapis.com/css2?family=Raleway:wght@400;500;600;700&family=Open+Sans:wght@400;600;700&display=swap" rel="stylesheet">
<style>
:root{
  --ink:#1f1f1f;
  --dark:#262626;
  --darker:#1b1b1b;
  --mid:#444;
  --text:#6a6a6a;
  --muted:#999;
  --line:#dcdcdc;
  --paper:#ffffff;
  --mist:#efefef;
  --photo-a:#b9b3ab;
  --photo-b:#7d7670;
}
*{box-sizing:border-box;margin:0;padding:0}
html,body{width:1200px;height:4306px;overflow:hidden}
body{font-family:"Open Sans",Arial,sans-serif;color:var(--ink);background:var(--paper);position:relative}
.abs{position:absolute}
h1,h2,h3,h4,.heading{font-family:"Raleway",Arial,sans-serif;color:var(--ink)}
p{font-size:14px;line-height:1.65;color:var(--text)}
.photo{position:absolute;background:linear-gradient(135deg,var(--photo-a),var(--photo-b))}

/* header */
.site-header{position:absolute;left:0;top:0;width:1200px;height:115px}
.brand{position:absolute;left:57px;top:22px;display:flex;align-items:center;gap:12px}
.brand-mark{width:14px;height:14px;background:var(--ink)}
.brand-name{font-family:"Raleway",sans-serif;font-weight:600;font-size:34px;line-height:1;color:var(--ink)}
.brand-sub{position:absolute;left:57px;top:66px;font-family:"Raleway",sans-serif;font-weight:600;font-size:11px;color:var(--ink)}
.contact{position:absolute;top:30px;display:flex;align-items:center;gap:16px}
.contact .ring{width:40px;height:40px;border:1px solid var(--line);border-radius:50%;display:flex;align-items:center;justify-content:center}
.contact b{display:block;font-size:12px;font-weight:700;color:var(--ink)}
.contact span{font-size:12px;color:var(--muted)}

/* nav */
.main-nav{position:absolute;left:57px;top:115px;width:1083px;height:43px;background:var(--darker);display:flex;align-items:center}
.main-nav a{font-family:"Raleway",sans-serif;font-size:12px;font-weight:700;color:#fff;text-decoration:none;text-transform:uppercase;padding:0 17px;height:43px;line-height:43px}
.main-nav a.active{background:#3a3a3a}
.main-nav .search{margin-left:auto;padding:0 26px}
.main-nav .quote{background:#3d3d3d;padding:0 30px}

/* hero */
.hero{left:0;top:158px;width:1200px;height:545px;background:linear-gradient(120deg,#d9d6d2,#9a928a 55%,#cfc9c2)}

/* welcome */
.welcome{position:absolute;left:0;top:703px;width:1200px;height:445px;background:var(--mist)}
.eyebrow{font-family:"Raleway",sans-serif;font-size:12px;font-weight:600;color:var(--ink)}
.welcome .eyebrow{position:absolute;top:73px;width:100%;text-align:center}
.welcome h2{position:absolute;top:98px;width:100%;text-align:center;font-size:46px;font-weight:500}
.welcome p{position:absolute;left:330px;top:170px;width:540px;text-align:center;font-size:13px}
.feature{position:absolute;top:272px;width:129px;height:159px;background:#fff;text-align:center}
.feature svg{margin-top:48px}
.feature span{display:block;margin-top:14px;font-family:"Raleway",sans-serif;font-size:13px;font-weight:600;color:var(--ink)}
.feature.raised{top:258px;height:170px;box-shadow:0 8px 22px rgba(0,0,0,.14);border-bottom:3px solid var(--ink)}
.feature.raised svg{margin-top:58px}

/* about */
.about{position:absolute;left:0;top:1148px;width:1200px;height:738px;background:#fff}
.about .eyebrow{position:absolute;left:57px;top:160px}
.about h2{position:absolute;left:57px;top:182px;font-size:48px;font-weight:500;line-height:1.2;width:420px}
.about p{position:absolute;left:57px;top:372px;width:535px;font-size:14px}
.btn{display:inline-block;font-family:"Raleway",sans-serif;font-size:13px;font-weight:600;color:#fff;background:var(--dark);text-align:center}
.about .btn{position:absolute;left:57px;top:514px;width:172px;height:52px;line-height:52px}
.about .call{position:absolute;left:290px;top:517px;display:flex;align-items:center;gap:16px;font-size:17px;font-weight:600}
.about .call .ring{width:46px;height:46px;border:1px solid var(--line);border-radius:50%;display:flex;align-items:center;justify-content:center}
.about .portrait{left:675px;top:58px;width:465px;height:580px;background:linear-gradient(160deg,#ece8e2,#c9c1b6 45%,#d8a637 75%,#c79a36)}
.video-tag{position:absolute;left:991px;top:498px;width:180px;height:96px;background:#fff;box-shadow:0 6px 18px rgba(0,0,0,.15);display:flex;align-items:center;gap:14px;padding-left:18px}
.video-tag b{font-family:"Raleway",sans-serif;font-size:17px;font-weight:600;line-height:1.15}

/* professional */
.pro{position:absolute;left:0;top:1886px;width:1200px;height:1242px;background:var(--mist)}
.pro-band{left:0;top:0;width:1200px;height:474px;background:linear-gradient(120deg,#4a4744,#2c2a28 50%,#565049)}
.pro-band::after{content:"";position:absolute;inset:0;background:rgba(20,20,20,.55)}
.pro .eyebrow{position:absolute;top:66px;width:100%;text-align:center;color:#fff;z-index:2}
.pro .title{position:absolute;top:88px;width:100%;text-align:center;font-family:"Raleway",sans-serif;font-size:58px;font-weight:600;color:#fff;z-index:2}
.pro .subtitle{position:absolute;top:150px;width:100%;text-align:center;font-family:"Raleway",sans-serif;font-size:34px;color:#e6e6e6;z-index:2}
.case-photo{left:57px;top:258px;width:537px;height:516px;background:linear-gradient(140deg,#cbc4bb,#8f8479 50%,#e7cfc0);z-index:2}
.case-card{position:absolute;left:594px;top:258px;width:546px;height:516px;background:#fff;padding:96px 0 0 38px;z-index:2}
.case-card h3{font-size:38px;font-weight:600;line-height:1.15;margin-top:10px}
.case-card p{width:440px;margin-top:20px;font-size:13px}
.case-card .actions{margin-top:26px;display:flex;align-items:center;gap:24px}
.case-card .btn{width:172px;height:50px;line-height:50px}
.case-card .more{font-family:"Raleway",sans-serif;font-size:13px;font-weight:600}
.steps-title{position:absolute;left:57px;top:850px;font-size:42px;font-weight:600;line-height:1.15}
.step{position:absolute;top:1010px;width:250px}
.step .head{display:flex;align-items:center;gap:18px}
.step .num{width:34px;height:34px;border-radius:50%;background:#fff;font-size:13px;display:flex;align-items:center;justify-content:center;color:var(--ink)}
.step .name{font-family:"Raleway",sans-serif;font-size:22px;font-weight:500}
.step p{margin-top:12px;font-size:13px;line-height:1.55}

/* articles */
.articles{position:absolute;left:0;top:3128px;width:1200px;height:761px;background:#fff}
.articles h2{position:absolute;left:57px;top:60px;font-size:44px;font-weight:600;line-height:1.18}
.post-main{position:absolute;left:57px;top:224px;width:546px;height:474px;background:#fff;box-shadow:0 4px 20px rgba(0,0,0,.12)}
.post-main .img{left:0;top:0;width:546px;height:232px;background:linear-gradient(130deg,#ddd7cf,#8d8378 50%,#d59a43)}
.post-main h3{position:absolute;top:268px;width:100%;text-align:center;font-size:21px;font-weight:600}
.post-main p{position:absolute;left:60px;top:308px;width:426px;text-align:center;font-size:13px}
.meta{font-size:13px;color:var(--text);display:flex;align-items:center;gap:8px}
.meta .count{width:22px;height:22px;border-radius:50%;background:#888;color:#fff;font-size:11px;display:flex;align-items:center;justify-content:center}
.post-main .meta{position:absolute;top:402px;width:100%;justify-content:center}
.post-side{position:absolute;left:654px;width:486px;height:230px}
.post-side .img{left:0;top:0;width:218px;height:230px}
.post-side .body{position:absolute;left:240px;top:18px;width:246px}
.post-side h4{font-size:17px;font-weight:600;line-height:1.3}
.post-side p{font-size:13px;margin-top:8px;line-height:1.55}
.post-side .meta{margin-top:10px}

/* footer */
.site-footer{position:absolute;left:0;top:3889px;width:1200px;height:359px;background:var(--darker);color:#bbb}
.site-footer .brand-name{position:absolute;left:57px;top:48px;font-size:30px;color:#ddd}
.site-footer .about-text{position:absolute;left:57px;top:112px;width:230px;font-size:12px;line-height:1.7;color:#aaa}
.socials{position:absolute;left:57px;top:245px;display:flex;gap:12px}
.socials i,.site-footer .fsoc i{display:block;width:28px;height:28px;border-radius:50%;border:1px solid #555}
.fcol{position:absolute;top:48px}
.fcol h4{font-size:19px;font-weight:500;color:#fff;margin-bottom:20px}
.fcol li{list-style:none;font-size:12px;color:#aaa;line-height:2.15;display:flex;align-items:center;gap:10px}
.fcol li::before{content:"";width:5px;height:5px;border-right:1px solid #aaa;border-bottom:1px solid #aaa;transform:rotate(-45deg)}
.news{display:flex;gap:14px;margin-bottom:22px;width:260px}
.news .thumb{width:58px;height:48px;flex:none;background:linear-gradient(135deg,#777,#444)}
.news b{display:block;font-size:13px;font-weight:500;color:#ddd;line-height:1.3}
.news span{display:block;font-size:11px;color:#888;line-height:1.45;margin-top:4px}
.subscribe p{font-size:12px;color:#aaa;width:250px}
.field{margin-top:18px;display:flex;width:250px;height:42px}
.field .input{flex:1;background:#2f2f2f}
.field .send{width:42px;background:#e8e8e8;display:flex;align-items:center;justify-content:center}
.fsoc{display:flex;gap:10px;margin-top:22px}
.fsoc i{width:22px!important;height:22px!important}
.legal{position:absolute;left:0;top:4248px;width:1200px;height:58px;background:#151515;font-size:12px;color:#999}
.legal .copy{position:absolute;left:57px;top:20px}
.legal nav{position:absolute;right:60px;top:20px;display:flex;gap:56px}
.legal nav a{font-size:11px;font-weight:700;color:#bbb;text-decoration:none;text-transform:uppercase}
</style>
</head>
<body>

<header class="site-header">
  <div class="brand"><span class="brand-mark"></span><span class="brand-name">Velto</span></div>
  <div class="brand-sub">Grounded Consulting</div>
  <div class="contact" style="left:470px">
    <div class="ring"><svg width="16" height="18" viewBox="0 0 16 18"><path d="M8 1a5.5 5.5 0 0 1 5.5 5.5C13.5 11 8 17 8 17S2.5 11 2.5 6.5A5.5 5.5 0 0 1 8 1z" fill="none" stroke="#333" stroke-width="1.4"/><circle cx="8" cy="6.5" r="2" fill="#333"/></svg></div>
    <div><b>48 Harbour Lane</b><span>Sydney NSW 2000</span></div>
  </div>
  <div class="contact" style="left:712px">
    <div class="ring"><svg width="16" height="16" viewBox="0 0 16 16"><path d="M3 1.5l3 3-1.6 1.8a9 9 0 0 0 5.3 5.3L11.5 10l3 3-1.8 1.8C7 15 1 9 1.2 3.3z" fill="none" stroke="#333" stroke-width="1.4"/></svg></div>
    <div><b>Call Us On</b><span>1-800-555-0142</span></div>
  </div>
  <div class="contact" style="left:928px">
    <div class="ring"><svg width="18" height="14" viewBox="0 0 18 14"><rect x="1" y="1" width="16" height="12" fill="none" stroke="#333" stroke-width="1.4"/><path d="M1 1l8 6 8-6" fill="none" stroke="#333" stroke-width="1.4"/></svg></div>
    <div><b>Mail Us @</b><span>hello@veltoconsult.com</span></div>
  </div>
</header>

<nav class="main-nav">
  <a class="active">Home</a><a>About Us</a><a>Services</a><a>Projects</a><a>Latest News</a><a>Products</a><a>My Account</a><a>Contact Us</a>
  <a class="search"><svg width="15" height="15" viewBox="0 0 15 15"><circle cx="6" cy="6" r="4.8" fill="none" stroke="#fff" stroke-width="1.8"/><path d="M9.6 9.6L14 14" stroke="#fff" stroke-width="1.8"/></svg></a>
  <a class="quote">Get A Quote</a>
</nav>

<div class="photo hero" role="img" aria-label="Consultant presenting a chart to a business team in a bright office"></div>

<section class="welcome">
  <div class="eyebrow">Welcome To Us</div>
  <h2>Top Consulting Agency</h2>
  <p>With over 30 years of Marketing, IT, and Business Solutions expertise, our goal is to partner with you to maximize your business reputation and IT infrastructure through our managed services and business solutions.</p>
  <div class="feature" style="left:57px">
    <svg width="36" height="36" viewBox="0 0 36 36" fill="none" stroke="#333" stroke-width="1.5"><rect x="8" y="6" width="18" height="24"/><path d="M12 12h10M12 17h10M12 22h6"/><rect x="4" y="14" width="8" height="8"/></svg>
    <span>Good Approach</span>
  </div>
  <div class="feature raised" style="left:287px">
    <svg width="36" height="36" viewBox="0 0 36 36" fill="none" stroke="#333" stroke-width="1.5"><path d="M18 8a7 7 0 0 0-4 12.8V25h8v-4.2A7 7 0 0 0 18 8z"/><path d="M15 28h6M18 2v3M6 14H3M33 14h-3M9 5l2 2M27 5l-2 2"/></svg>
    <span>Great Ideas</span>
  </div>
  <div class="feature" style="left:508px">
    <svg width="36" height="36" viewBox="0 0 36 36" fill="none" stroke="#333" stroke-width="1.5"><ellipse cx="18" cy="20" rx="11" ry="8"/><path d="M24 13l3-5M10 27v4M26 27v4"/><circle cx="23" cy="18" r="1" fill="#333"/></svg>
    <span>Save Money</span>
  </div>
  <div class="feature" style="left:746px">
    <svg width="36" height="36" viewBox="0 0 36 36" fill="none" stroke="#333" stroke-width="1.5"><circle cx="18" cy="18" r="5"/><path d="M18 5v5M18 26v5M5 18h5M26 18h5M9 9l3.5 3.5M23.5 23.5L27 27M27 9l-3.5 3.5M12.5 23.5L9 27"/><circle cx="18" cy="18" r="10"/></svg>
    <span>Easy Customize</span>
  </div>
  <div class="feature" style="left:967px">
    <svg width="36" height="36" viewBox="0 0 36 36" fill="none" stroke="#333" stroke-width="1.5"><path d="M10 4h12l6 6v22H10z"/><path d="M22 4v6h6M14 16h10M14 21h10M14 26h6"/><path d="M6 8v26h18"/></svg>
    <span>Detailed Report</span>
  </div>
</section>

<section class="about">
  <div class="eyebrow">What We Do</div>
  <h2>Welcome To Our Consulting Agency</h2>
  <p>We solve business problems, take a consultative approach to every client engagement, and find actionable solutions that will help your organization achieve the best business outcomes. We know the importance of delivering the best customer experience and we enable your organization to exceed customer expectations.</p>
  <a class="btn">Read More</a>
  <div class="call"><span class="ring"><svg width="16" height="16" viewBox="0 0 16 16"><path d="M3 1.5l3 3-1.6 1.8a9 9 0 0 0 5.3 5.3L11.5 10l3 3-1.8 1.8C7 15 1 9 1.2 3.3z" fill="#333"/></svg></span>0 800 555 01 77</div>
  <div class="photo portrait" role="img" aria-label="Smiling consultant in a yellow top holding a tablet"></div>
  <div class="video-tag">
    <svg width="40" height="30" viewBox="0 0 40 30" fill="none" stroke="#333" stroke-width="1.6"><rect x="2" y="3" width="36" height="24" rx="3"/><path d="M16 10v10l9-5z" fill="#333"/></svg>
    <b>Video<br>About Us</b>
  </div>
</section>

<section class="pro">
  <div class="photo pro-band" role="img" aria-label="Office team working together, darkened background"></div>
  <div class="eyebrow">We Are Professionals</div>
  <div class="title">Professional Approach</div>
  <div class="subtitle">and Quality Services</div>
  <div class="photo case-photo" role="img" aria-label="Smiling businesswoman seated at a desk with a computer"></div>
  <div class="case-card">
    <div class="eyebrow">Case Studies</div>
    <h3>Business Management<br>Case Studies</h3>
    <p>Lorem ipsum dolor sit amet, ei qui essent pericula convenire phaedrum lorem ipsum dolor sit amet, ei qui essent pericula convenire, ei qui essent pericula convenire phaedrum lorem ipsum dolor sit amet, ei qui essent pericula it amet, ei qui essent pericula convenire phaedrum lorem ipsum dolor sit amet, ei qui essent pericula convenire.</p>
    <div class="actions"><a class="btn">Read More</a><span class="more">Know More</span></div>
  </div>

  <h2 class="steps-title">4 Steps To Make<br>Successful Business</h2>
  <div class="step" style="left:57px"><div class="head"><span class="num">1</span><span class="name">Analize</span></div><p>Lorem ipsum dolor sit amet, ei qui essent pericula convenire phaedrum lorem ipsum dolor sit amet, ei qui essent pericula convenire.</p></div>
  <div class="step" style="left:344px"><div class="head"><span class="num">2</span><span class="name">Advise</span></div><p>Lorem ipsum dolor sit amet, ei qui essent pericula convenire phaedrum lorem ipsum dolor sit amet, ei qui essent pericula convenire.</p></div>
  <div class="step" style="left:631px"><div class="head"><span class="num">3</span><span class="name">Strategy</span></div><p>Lorem ipsum dolor sit amet, ei qui essent pericula convenire phaedrum lorem ipsum dolor sit amet, ei qui essent pericula convenire.</p></div>
  <div class="step" style="left:910px"><div class="head"><span class="num">4</span><span class="name">Result</span></div><p>Lorem ipsum dolor sit amet, ei qui essent pericula convenire phaedrum lorem ipsum dolor sit amet, ei qui essent pericula convenire.</p></div>
</section>

<section class="articles">
  <h2>Read Our Latest Articles,<br>Tips &amp; News</h2>
  <article class="post-main">
    <div class="photo img" role="img" aria-label="Group of smiling colleagues standing together"></div>
    <h3>What Planning Process Needs?</h3>
    <p>We solve business problems, take a consultative approach to every client engagement, and find actionable solutions that will help your organization achieve</p>
    <div class="meta"><span class="count">0</span>comments &nbsp;|&nbsp; by velto_admin</div>
  </article>
  <article class="post-side" style="top:224px">
    <div class="photo img" role="img" aria-label="Consultant in yellow holding a tablet" style="background:linear-gradient(150deg,#e6e1da,#c8a24a)"></div>
    <div class="body">
      <h4>7 Tips To Move Your Project Forward.</h4>
      <p>We solve business problems, take a consultative approach to every client engagement, and find actionable</p>
      <div class="meta"><span class="count">0</span>comments &nbsp;|&nbsp; by velto_admin</div>
    </div>
  </article>
  <article class="post-side" style="top:474px">
    <div class="photo img" role="img" aria-label="Smiling professional working at a laptop" style="background:linear-gradient(150deg,#d8d4cf,#8b8e98)"></div>
    <div class="body">
      <h4>Don't Worry About Creativity spiration.</h4>
      <p>We solve business problems, take a consultative approach to every client engagement, and find actionable</p>
      <div class="meta"><span class="count">0</span>comments &nbsp;|&nbsp; by velto_admin</div>
    </div>
  </article>
</section>

<footer class="site-footer">
  <div class="brand-name">Velto</div>
  <p class="about-text">Over 24 years of experience and one of the region's trusted advisers, helping logistics, sales and industrial teams plan with care, train their people and deliver the best results.</p>
  <div class="socials"><i></i><i></i><i></i><i></i><i></i></div>

  <div class="fcol" style="left:359px">
    <h4>SERVICES</h4>
    <ul><li>Chemical Research</li><li>Material Science</li><li>Petroleum and Gas</li><li>Mechanical Engineering</li><li>Agriculture Processing</li><li>Power and Energy</li></ul>
  </div>
  <div class="fcol" style="left:611px">
    <h4>RECENT NEWS</h4>
    <div class="news"><div class="thumb" role="img" aria-label="News thumbnail"></div><div><b>Their House Is A Museum Where.</b><span>We solve business problems, take a consultative approach to every</span></div></div>
    <div class="news"><div class="thumb" role="img" aria-label="News thumbnail"></div><div><b>Got A Dream And We Just...</b><span>We solve business problems, take a consultative approach to every</span></div></div>
  </div>
  <div class="fcol subscribe" style="left:890px">
    <h4>SUBSCRIBE US</h4>
    <p>Subscribe to our newsletter!</p>
    <div class="field"><span class="input"></span><span class="send"><svg width="16" height="16" viewBox="0 0 16 16"><path d="M1 8l14-6-5 13-2-5z" fill="#333"/></svg></span></div>
    <p style="margin-top:16px;line-height:1.6">We don't do spam and your mail is kept confidential.</p>
    <div class="fsoc"><i></i><i></i><i></i><i></i><i></i></div>
  </div>
</footer>
<div class="legal">
  <span class="copy">Copyright © 2018 All rights reserved</span>
  <nav><a>Home</a><a>Services</a><a>Term &amp; Condition</a><a>Privacy Policy</a><a>Contact Us</a></nav>
</div>

</body>
</html>
```